Brookvale Homes Flyer

Quarter-page leave-behind flyer for a commercial cleaning company (print)

ABOUT US
Quillon Commercial Cleaning is a Texas-owned commercial cleaning company serving Austin for over 20 years. We were recently named to Brookvale Homes's Capital Partner Roster Circle, a preferred vendor program covering apartment communities across the Austin metro. Our sales team will hand this flyer to apartment community managers during property visits.

THE JOB THIS FLYER MUST DO
A busy property manager should scan it in five seconds, understand what we do, trust us and keep the card on their desk. The call to action is booking a free walkthrough of their community. Do not include any pricing.

SPECS
Size: 4.25 x 5.5 inches (quarter of a letter page), single sided, portrait. Print ready with 0.125 inch bleed, CMYK, 300 dpi minimum. Vector preferred.

REQUIRED CONTENT
Headline: The clean your residents notice.
Badge or tagline: Brookvale Homes's Approved Austin Cleaning Company.
Supporting line: Preferred Vendor Partner in BVH's Capital Partner Roster Circle. Texas-owned, serving Austin for 20+ years.
Services (icons welcome): recurring janitorial, floor strip wax and buff, carpet extraction, windows and glass, upholstery care, pressure washing, move-in and move-out cleans, damage restoration.
Trust points: licensed and insured, background-checked crews, TrudeLink compliant, invoicing through Supplier Nook and Halvex Systems.

Social proof line: Already trusted by BVH communities. Ask your peers at The Wendlow and The Fennick on Garrow.

Call to action: Book a free walkthrough of your community. Call or email 512-555-0147 or support@quillonclean-example.com

STYLE DIRECTION
Clean, crisp and premium. Whiteness and shine should feel like part of the message. We like a deep green and teal palette with one warm accent, but strong alternative directions are welcome. Custom icons over clip art.
AVOID
Stock photos of cleaners with buckets, cartoon mascots, sparkle overload, cluttered layouts, any prices or dollar amounts.
DELIVERABLES
Print-ready PDF with bleed and crop marks, plus editable source files (AI, PSD or Figma). A version with our logo placement marked, since we will supply the logo file to the winner.

```html
<!DOCTYPE html>
<html lang="en">
<head>
<meta charset="utf-8">
<title>Quillon Commercial Cleaning – Brookvale Homes Flyer</title>
<link href="https://fonts.googleapis.com/css2?family=Montserrat:wght@400;600;700;800&family=Lato:wght@400&display=swap" rel="stylesheet">
<style>
  :root {
    --deep-green: #0a4a3a;
    --brand-green: #41b649;
    --panel-green: #e3f2e4;
    --faint-green: #9ed6a3;
    --teal-dark: #066b5e;
    --teal-light: #139080;
    --ink: #333333;
    --white: #ffffff;
  }
  * { margin: 0; padding: 0; box-sizing: border-box; }
  html, body { width: 927px; height: 1200px; overflow: hidden; background: var(--white); }
  .flyer { position: relative; width: 927px; height: 1200px; overflow: hidden; background: var(--white); font-family: 'Lato', sans-serif; color: var(--ink); }
  .decor { position: absolute; inset: 0; }
  .abs { position: absolute; }
  .brand-name { left: 40px; top: 150px; font-family: 'Montserrat', sans-serif; font-weight: 700; font-size: 74px; color: var(--brand-green); letter-spacing: -1px; }
  .headline { left: 40px; top: 296px; font-family: 'Montserrat', sans-serif; font-weight: 800; font-size: 58px; line-height: 70px; color: var(--deep-green); }
  .tagline { left: 40px; top: 440px; font-family: 'Montserrat', sans-serif; font-weight: 400; font-size: 33px; line-height: 40px; color: var(--brand-green); }
  .support { left: 40px; top: 540px; font-size: 24px; line-height: 33px; color: var(--ink); }
  .section-title { font-family: 'Montserrat', sans-serif; font-weight: 700; font-size: 29px; color: var(--deep-green); }
  .services-title { left: 40px; top: 624px; }
  .service-icon { position: absolute; width: 67px; height: 67px; border-radius: 50%; background: var(--brand-green); display: flex; align-items: center; justify-content: center; }
  .service-icon svg { width: 40px; height: 40px; }
  .service-label { position: absolute; font-size: 22px; line-height: 26px; color: var(--deep-green); transform: translateY(-50%); }
  .trust-title { left: 40px; top: 876px; }
  .trust-list { left: 40px; top: 925px; list-style: none; }
  .trust-list li { position: relative; padding-left: 30px; font-size: 22px; line-height: 35px; }
  .trust-list li::before { content: ""; position: absolute; left: 1px; top: 13px; width: 10px; height: 10px; border-radius: 50%; background: var(--brand-green); }
  .proof-mark { left: 446px; top: 902px; font-family: 'Montserrat', sans-serif; font-weight: 700; font-size: 34px; color: var(--faint-green); letter-spacing: -0.5px; }
  .proof-title { left: 583px; top: 920px; font-family: 'Montserrat', sans-serif; font-weight: 700; font-size: 28px; line-height: 33px; color: var(--deep-green); }
  .proof-text { left: 583px; top: 996px; font-family: 'Montserrat', sans-serif; font-weight: 400; font-size: 18px; line-height: 29px; color: var(--brand-green); }
  .cta { left: 45px; top: 1132px; font-family: 'Montserrat', sans-serif; font-weight: 700; font-size: 24px; line-height: 28px; color: var(--white); }
  .cta .accent { color: var(--brand-green); }
  .contact-icon { position: absolute; width: 40px; height: 40px; border-radius: 50%; background: var(--brand-green); display: flex; align-items: center; justify-content: center; }
  .contact-icon svg { width: 22px; height: 22px; }
  .contact-label { font-family: 'Montserrat', sans-serif; font-weight: 600; font-size: 16px; color: var(--brand-green); }
  .contact-value { font-size: 12.5px; color: var(--white); margin-top: 3px; }
</style>
</head>
<body>
<div class="flyer">
  <svg class="decor" viewBox="0 0 1275 1650" width="927" height="1200" preserveAspectRatio="none">
    <polygon points="470,0 1275,0 1275,740" fill="url(#skyline)" role="img" aria-label="Photo of glass office towers seen from below, in teal tones"/>
    <defs>
      <linearGradient id="skyline" x1="0" y1="0" x2="1" y2="1">
        <stop offset="0" stop-color="#0a8a74"/>
        <stop offset="1" stop-color="#055f57"/>
      </linearGradient>
    </defs>
    <polygon points="265,0 470,0 660,176 660,322" fill="#0a4a3a"/>
    <polygon points="222,0 245,0 515,222 497,230" fill="#41b649"/>
    <polygon points="0,0 100,0 212,155 127,157 0,62" fill="#41b649"/>
    <polygon points="510,1215 1275,1215 1275,1505 745,1505" fill="#e3f2e4"/>
    <polygon points="0,1540 1197,1540 1090,1650 0,1650" fill="#0a4a3a"/>
    <polygon points="1186,1562 1196,1562 1110,1650 1100,1650" fill="#41b649"/>
    <polygon points="1275,1548 1275,1650 1172,1650" fill="#41b649"/>
  </svg>

  <div class="abs brand-name">Quillon</div>

  <h1 class="abs headline">The Clean Your<br>Residents Notice</h1>
  <p class="abs tagline">Brookvale Homes's Approved Austin<br>Cleaning Company.</p>
  <p class="abs support">Preferred Vendor Partner in BVH's Capital Partner Roster<br>Circle. Texas-owned, serving Austin for 20+ years.</p>

  <h2 class="abs section-title services-title">Our Services</h2>

  <!-- Row 1 -->
  <div class="service-icon" style="left:40px;top:679px">
    <svg viewBox="0 0 40 40" fill="none" stroke="#fff" stroke-width="2"><rect x="8" y="14" width="10" height="20" rx="2"/><path d="M10 14V9h6v5M16 9h5"/><rect x="22" y="20" width="11" height="14" rx="2"/><circle cx="30" cy="10" r="3"/></svg>
  </div>
  <div class="service-label" style="left:125px;top:712px">Recurring<br>Janitorial</div>

  <div class="service-icon" style="left:256px;top:679px">
    <svg viewBox="0 0 40 40" fill="none" stroke="#fff" stroke-width="2"><rect x="9" y="20" width="20" height="9" rx="2"/><path d="M19 20V10h10M29 7v6M8 33h24"/></svg>
  </div>
  <div class="service-label" style="left:340px;top:712px">Floor Strip,<br>Wax &amp; Buff</div>

  <div class="service-icon" style="left:485px;top:679px">
    <svg viewBox="0 0 40 40" fill="none" stroke="#fff" stroke-width="2"><rect x="7" y="9" width="26" height="24" rx="2"/><path d="M20 5v18M13 23h14v5H13z"/></svg>
  </div>
  <div class="service-label" style="left:570px;top:712px">Carpet<br>Extraction</div>

  <div class="service-icon" style="left:705px;top:679px">
    <svg viewBox="0 0 40 40" fill="none" stroke="#fff" stroke-width="2"><rect x="12" y="6" width="22" height="22"/><path d="M23 6v22M12 17h22M6 34l10-10"/></svg>
  </div>
  <div class="service-label" style="left:790px;top:712px">Windows<br>&amp; Glass</div>

  <!-- Row 2 -->
  <div class="service-icon" style="left:40px;top:774px">
    <svg viewBox="0 0 40 40" fill="none" stroke="#fff" stroke-width="2"><path d="M11 20v-7a3 3 0 0 1 3-3h12a3 3 0 0 1 3 3v7"/><rect x="7" y="19" width="26" height="9" rx="3"/><path d="M10 28v5M30 28v5"/></svg>
  </div>
  <div class="service-label" style="left:125px;top:807px">Upholstery<br>Care</div>

  <div class="service-icon" style="left:256px;top:774px">
    <svg viewBox="0 0 40 40" fill="none" stroke="#fff" stroke-width="2"><rect x="5" y="17" width="12" height="6" rx="1"/><path d="M17 20h7M26 14l6-4M26 20h8M26 26l6 4"/></svg>
  </div>
  <div class="service-label" style="left:340px;top:807px">Pressure<br>Washing</div>

  <div class="service-icon" style="left:485px;top:774px">
    <svg viewBox="0 0 40 40" fill="none" stroke="#fff" stroke-width="2"><path d="M6 19L20 7l14 12M10 16v17h20V16"/><rect x="17" y="23" width="6" height="10"/></svg>
  </div>
  <div class="service-label" style="left:570px;top:807px">Move-In &amp;<br>Move-Out<br>Cleans</div>

  <div class="service-icon" style="left:705px;top:774px">
    <svg viewBox="0 0 40 40" fill="none" stroke="#fff" stroke-width="2"><path d="M20 5l12 5v9c0 8-5 13-12 16C13 32 8 27 8 19v-9z"/><path d="M14 20l4 4 8-8"/></svg>
  </div>
  <div class="service-label" style="left:790px;top:807px">Damage<br>Restoration</div>

  <h2 class="abs section-title trust-title">Clean That Shows</h2>
  <ul class="abs trust-list">
    <li>Licensed &amp; Insured</li>
    <li>Background-Checked Crews</li>
    <li>TrudeLink Compliant</li>
    <li>Invoicing Through Supplier Nook</li>
    <li>Halvex Systems</li>
  </ul>

  <div class="abs proof-mark">Quillon</div>
  <h2 class="abs proof-title">Already Trusted by<br>BVH Communities</h2>
  <p class="abs proof-text">Ask your peers at The Wendlow<br>and The Fennick on Garrow.</p>

  <p class="abs cta"><span class="accent">Book a Free Walkthrough</span><br>of Your Community.</p>

  <div class="contact-icon" style="left:405px;top:1140px">
    <svg viewBox="0 0 24 24" fill="#fff"><path d="M6.6 10.8a15 15 0 0 0 6.6 6.6l2.2-2.2a1 1 0 0 1 1-.25 11 11 0 0 0 3.6.57 1 1 0 0 1 1 1V20a1 1 0 0 1-1 1A17 17 0 0 1 3 4a1 1 0 0 1 1-1h3.5a1 1 0 0 1 1 1c0 1.25.2 2.45.57 3.57a1 1 0 0 1-.25 1z"/></svg>
  </div>
  <div class="abs" style="left:455px;top:1141px">
    <div class="contact-label">Call Us</div>
    <div class="contact-value">512-555-0147</div>
  </div>

  <div class="contact-icon" style="left:565px;top:1140px">
    <svg viewBox="0 0 24 24" fill="#fff"><path d="M3 6h18v12H3z" fill="none" stroke="#fff" stroke-width="2"/><path d="M3 6l9 7 9-7"  fill="none" stroke="#fff" stroke-width="2"/></svg>
  </div>
  <div class="abs" style="left:615px;top:1141px">
    <div class="contact-label">Email</div>
    <div class="contact-value">support@quillonclean-example.com</div>
  </div>
</div>
</body>
</html>
```